Swing Dance Themed Cleaning Company Website

We need a website designed for a cleaning company based in Portland, Oregon called Foxtrot Lane. We clean homes and commercial buildings, inside and out.

needs to be vintage and like the velvet moonbeam. Speakeasy 1920s feel.
needs to be classy.

Check out foxtrotlane.com We are not happy with the site currently.

please look at house scout site for more content https://www.housescoutly.com/rated.FoxtrotLaneCleaning.41827463.html

Check out my videos on my ClipTube channel Foxtrot Lane

Target Market(s)

middle class and home owner

Industry/Entity Type

Cleaning Service

Number of Pages Required

3 page

Font styles to use
Other font styles liked:
• jazzrag

Colors

Designer to choose colors to be used in the design.

Requirements
Must have
• must be good on pc and mobile

```html
<!DOCTYPE html>
<html lang="en">
<head>
<meta charset="utf-8">
<title>Foxtrot Lane — Portland's Classiest Cleaners</title>
<link href="https://fonts.googleapis.com/css2?family=Poiret+One&family=Montserrat:wght@400;600&display=swap" rel="stylesheet">
<style>
:root{
  --ink:#1f1d1c;
  --ink-deep:#171514;
  --brown:#3a2a24;
  --brown-dark:#281d19;
  --gold:#b8903f;
  --gold-light:#d4ae5c;
  --gold-deep:#9c7832;
  --paper:#ffffff;
  --muted:#a9a39b;
  --line:#6b6258;
}
*{box-sizing:border-box;margin:0;padding:0}
html,body{width:1200px;height:4336px;overflow:hidden;background:var(--ink)}
body{position:relative;font-family:"Montserrat",Arial,sans-serif;color:var(--paper)}
.deco{font-family:"Poiret One","Century Gothic",sans-serif;font-weight:400;text-transform:uppercase;letter-spacing:2px}
section,header,footer{position:absolute;left:0;width:1200px}
.abs{position:absolute}

/* hero */
.hero{top:0;height:640px}
.hero-photo{position:absolute;inset:0;background:linear-gradient(180deg,#5a4330 0%,#8a6544 45%,#6e4e35 75%,#3b2c22 100%)}
.brand{position:absolute;left:88px;top:34px;display:flex;align-items:center;gap:12px}
.brand-mark{width:26px;height:26px;border-radius:50%;background:var(--paper)}
.brand-name{font-family:"Poiret One",sans-serif;font-size:24px;letter-spacing:2px;text-transform:uppercase;color:var(--paper)}
.brand-tag{position:absolute;left:88px;top:70px;font-size:9px;letter-spacing:1px;color:var(--paper);text-transform:uppercase}
.nav{position:absolute;right:100px;top:50px;display:flex;gap:24px;font-size:11px;text-transform:uppercase;letter-spacing:1px}
.nav a{color:var(--paper);text-decoration:none}
.nav a.active{border-bottom:1px solid var(--paper);padding-bottom:3px}
.hero-arrow{position:absolute;top:320px}
.banner{position:absolute;left:370px;top:250px;width:460px;height:110px}
.banner-text{position:absolute;left:370px;top:266px;width:460px;text-align:center}
.banner-title{font-size:26px;color:var(--paper);letter-spacing:3px}
.banner-sub{font-size:15px;margin-top:8px;color:var(--paper)}
.dots{position:absolute;top:674px;left:0;width:1200px;display:flex;justify-content:center;gap:8px;z-index:2}
.dots span{width:7px;height:7px;border-radius:50%;background:var(--muted)}
.dots span.on{background:var(--paper)}

/* section headings */
.sec-title{position:absolute;left:0;width:1200px;text-align:center;font-size:32px}
.sec-sub{position:absolute;left:0;width:1200px;text-align:center;font-size:13px;color:var(--muted)}
.rule{position:absolute;left:530px;width:140px;height:14px}

/* about */
.about{top:640px;height:740px;background:var(--ink)}
.about h3{position:absolute;left:88px;top:276px;font-size:30px;color:var(--gold)}
.about h4{position:absolute;left:88px;top:314px;font-size:24px;font-weight:400}
.about p{position:absolute;left:88px;top:360px;width:500px;font-size:12px;line-height:21px;color:var(--muted)}
.btn-small{position:absolute;background:var(--gold);color:var(--paper);font-size:11px;text-transform:uppercase;text-align:center;letter-spacing:1px}
.review-link{position:absolute;left:226px;top:512px;font-size:12px;color:var(--paper);display:flex;align-items:center;gap:8px}
.video{position:absolute;left:652px;top:260px;width:460px;height:320px;background:#111}
.video-frame{position:absolute;left:0;top:0;width:460px;height:290px;background:linear-gradient(110deg,#5a4a3e 0%,#8d7a66 45%,#cdbfae 70%,#4a3d33 100%)}
.video-bar{position:absolute;left:0;top:290px;width:460px;height:30px;background:#0e0e0e}

/* contact */
.contact{top:1380px;height:540px;overflow:hidden}
.contact-bg{position:absolute;inset:0;background:radial-gradient(ellipse at 20% 70%,#4a3830 0%,var(--brown) 40%,var(--brown-dark) 100%)}
.contact .intro{position:absolute;left:300px;top:88px;width:600px;text-align:center;font-size:11px;line-height:18px;color:#cfc6bb}
.field{position:absolute;font-size:11px;color:var(--paper);border-bottom:1px solid #bfb4a6;height:26px}
.submit{position:absolute;left:336px;top:432px;width:488px;height:36px;line-height:36px;background:var(--gold);text-align:center;font-size:13px;letter-spacing:2px;text-transform:uppercase}

/* services */
.services{top:1920px;height:832px;background:var(--ink)}
.services .intro{position:absolute;left:300px;top:132px;width:600px;text-align:center;font-size:11px;line-height:18px;color:var(--muted)}
.svc{position:absolute;top:280px;width:240px}
.svc-photo{width:240px;height:280px}
.svc h5{margin-top:26px;font-size:16px;font-family:"Poiret One",sans-serif;text-transform:uppercase;letter-spacing:1px;font-weight:400}
.svc p{margin-top:10px;font-size:11px;line-height:18px;color:var(--muted)}

/* call to action */
.cta{top:2752px;height:368px;background:linear-gradient(180deg,var(--gold-light),var(--gold) 50%,var(--gold-deep))}
.cta-line{position:absolute;left:0;width:1200px;text-align:center}
.cta-lead{top:80px;font-size:24px;line-height:30px}
.cta-phone{top:184px;font-size:40px;font-weight:600;letter-spacing:1px}
.cta-mail{top:242px;font-size:14px}
.btn-dark{position:absolute;left:510px;top:300px;width:180px;height:34px;line-height:34px;background:var(--ink);color:var(--paper);text-align:center;font-size:11px;font-weight:600;letter-spacing:1px;text-transform:uppercase}

/* blog */
.blog{top:3120px;height:772px;background:var(--ink)}
.post{position:absolute;top:248px;width:504px;height:320px}
.post-photo{position:absolute;inset:0}
.post-date{position:absolute;right:20px;top:0;width:70px;height:82px;background:var(--gold);text-align:center;padding-top:12px;font-family:"Poiret One",sans-serif;font-size:18px;line-height:28px}
.post-date b{display:block;font-size:30px;font-weight:400}
.post-title{position:absolute;left:28px;bottom:26px;width:420px;font-size:20px;line-height:26px}

/* footer */
.site-footer{top:3892px;height:444px;background:linear-gradient(180deg,var(--gold),var(--gold-deep))}
.foot-brand{position:absolute;left:120px;top:100px;display:flex;align-items:center;gap:12px}
.foot-tag{position:absolute;left:120px;top:140px;font-size:9px;letter-spacing:1px;text-transform:uppercase}
.foot-copy{position:absolute;left:120px;top:176px;font-size:11px}
.foot-col{position:absolute;left:440px;font-size:11px;line-height:17px}
.foot-col h6{font-size:10px;font-weight:600;text-transform:uppercase;letter-spacing:1px;margin-bottom:2px}
.foot-about{position:absolute;left:740px;top:76px;width:340px;font-size:11px;line-height:18px}
.foot-about h6{font-size:10px;font-weight:600;text-transform:uppercase;letter-spacing:1px;margin-bottom:4px}
.social{position:absolute;left:740px;top:296px;display:flex;gap:14px}
.social span{width:18px;height:18px;border-radius:50%;background:var(--paper)}
</style>
</head>
<body>

<header class="hero">
  <div class="hero-photo" role="img" aria-label="Photo of a cleaner vacuuming a warm wood-panelled living room"></div>
  <div class="brand"><span class="brand-mark"></span><span class="brand-name">Foxtrot Lane</span></div>
  <div class="brand-tag">Classiest cleaners in Portland</div>
  <nav class="nav">
    <a class="active" href="#">Home</a><a href="#">Contact us</a><a href="#">About us</a><a href="#">Our update</a>
  </nav>
  <svg class="hero-arrow" style="left:28px" width="16" height="28" viewBox="0 0 16 28"><path d="M13 2 3 14l10 12" fill="none" stroke="#fff" stroke-width="2"/></svg>
  <svg class="hero-arrow" style="right:28px" width="16" height="28" viewBox="0 0 16 28"><path d="M3 2l10 12L3 26" fill="none" stroke="#fff" stroke-width="2"/></svg>
  <svg class="banner" viewBox="0 0 460 110">
    <polygon points="0,20 40,20 40,90 0,90 16,55" fill="#9c7832"/>
    <polygon points="460,20 420,20 420,90 460,90 444,55" fill="#9c7832"/>
    <rect x="24" y="8" width="412" height="90" fill="#c29a48"/>
  </svg>
  <div class="banner-text">
    <div class="banner-title deco">Foxtrot Lane Portland's</div>
    <div class="banner-sub">Classiest cleaners outdoor indoor</div>
  </div>
</header>
<div class="dots"><span></span><span class="on"></span><span></span></div>

<section class="about">
  <h2 class="sec-title deco" style="top:70px">About us Foxtrot Lane</h2>
  <div class="sec-sub" style="top:116px">Making the greater Portland area clean, one building at a time</div>
  <svg class="rule" style="top:150px" viewBox="0 0 140 14"><line x1="0" y1="7" x2="62" y2="7" stroke="#b8903f"/><circle cx="70" cy="7" r="4" fill="none" stroke="#b8903f"/><line x1="78" y1="7" x2="140" y2="7" stroke="#b8903f"/></svg>
  <h3 class="deco">Good people, great service</h3>
  <h4>Cleaning and maintenance</h4>
  <p>Foxtrot Lane is a locally owned family business devoted to providing you with quality cleaning services for a reasonable price. We proudly clean homes and commercial buildings across Portland, inside and out, with the care of a good neighbour. Our friendly crew arrives on time, treats every room with respect and leaves each space bright, fresh and ready for company. We have kept that simple promise for years.</p>
  <div class="btn-small" style="left:88px;top:506px;width:110px;height:28px;line-height:28px">Read more</div>
  <div class="review-link">
    <svg width="14" height="14" viewBox="0 0 14 14"><path d="M7 1l1.8 3.9 4.2.4-3.2 2.8.9 4.1L7 10.1 3.3 12.2l.9-4.1L1 5.3l4.2-.4z" fill="#b8903f"/></svg>
    Leave a Review
  </div>
  <div class="video">
    <div class="video-frame" role="img" aria-label="Video still of a cleaner wiping a tall window"></div>
    <div class="video-bar">
      <svg width="460" height="30" viewBox="0 0 460 30"><path d="M12 9v12l10-6z" fill="#fff"/><rect x="36" y="14" width="320" height="2" fill="#555"/><rect x="36" y="14" width="90" height="2" fill="#fff"/><rect x="372" y="10" width="14" height="10" fill="none" stroke="#fff"/><rect x="400" y="10" width="14" height="10" fill="#fff"/><rect x="428" y="9" width="18" height="12" fill="none" stroke="#fff"/></svg>
    </div>
  </div>
</section>

<section class="contact">
  <div class="contact-bg" role="img" aria-label="Dark brown damask pattern with a faint silhouette of a 1920s dancer"></div>
  <h2 class="sec-title deco" style="top:40px">Contact us</h2>
  <p class="intro">We are a family-owned crew serving homes and businesses across Portland. Send us a note about your space and timing, and we will reply within one business day with a friendly, honest estimate for your cleaning needs.</p>
  <div class="field" style="left:340px;top:196px;width:230px">Name</div>
  <div class="field" style="left:610px;top:196px;width:230px">Email</div>
  <div class="field" style="left:340px;top:248px;width:500px">Subject</div>
  <div class="field" style="left:340px;top:300px;width:500px">Message</div>
  <div class="submit">Submit</div>
</section>

<section class="services">
  <h2 class="sec-title deco" style="top:100px">Our services</h2>
  <p class="intro">We provide cleaning and janitorial services for one-time and recurring needs. From the first visit we tailor a plan to your space, so every room is cared for the way you like it.</p>
  <div class="svc" style="left:88px"><div class="svc-photo" role="img" aria-label="Photo of a green broom sweeping a wooden floor" style="background:linear-gradient(160deg,#c98c4f,#8a5a33 60%,#2f6b52)"></div><h5>Janitorial services</h5><p>Routine janitorial, floor care, restroom sanitation and trash removal.</p></div>
  <div class="svc" style="left:352px"><div class="svc-photo" role="img" aria-label="Photo of a mop cleaning a tiled floor" style="background:linear-gradient(160deg,#3a3432,#6d625b 55%,#2a2523)"></div><h5>House cleaning</h5><p>Routine dusting, kitchen care, bathroom scrubbing and full deep cleans.</p></div>
  <div class="svc" style="left:616px"><div class="svc-photo" role="img" aria-label="Photo of a hand holding a paint brush" style="background:linear-gradient(160deg,#e9e6e2,#b5aea6 55%,#6f6862)"></div><h5>Maintenance</h5><p>Routine touch-ups, window washing, pressure washing and light repairs.</p></div>
  <div class="svc" style="left:880px"><div class="svc-photo" role="img" aria-label="Photo of coloured stage lights at an evening event" style="background:radial-gradient(circle at 30% 35%,#3e8a3a,transparent 30%),radial-gradient(circle at 75% 30%,#b33a2c,transparent 30%),#1a1512"></div><h5>Event services</h5><p>Routine setup, venue tidying, guest area care and after-party cleanup.</p></div>
</section>

<section class="cta">
  <div class="cta-line cta-lead deco">To schedule an appointment or get an<br>estimate call</div>
  <div class="cta-line cta-phone">503-555-0148</div>
  <div class="cta-line cta-mail">hello@foxtrotlane.com | www.foxtrotlane.com</div>
  <div class="btn-dark">Make an appointment</div>
</section>

<section class="blog">
  <h2 class="sec-title deco" style="top:110px">Blog</h2>
  <div class="sec-sub" style="top:156px">The latest news from Foxtrot Lane</div>
  <svg class="rule" style="top:184px" viewBox="0 0 140 14"><line x1="0" y1="7" x2="62" y2="7" stroke="#b8903f"/><circle cx="70" cy="7" r="4" fill="none" stroke="#b8903f"/><line x1="78" y1="7" x2="140" y2="7" stroke="#b8903f"/></svg>
  <article class="post" style="left:88px">
    <div class="post-photo" role="img" aria-label="Photo of a guitarist performing on an outdoor festival stage" style="background:linear-gradient(180deg,#4d6b3a,#3a3a33 55%,#1c1a18)"></div>
    <div class="post-date">July<b>15</b></div>
    <h3 class="post-title deco">Foxtrot Lane returns to Riverside Rhythm Festival 2017</h3>
  </article>
  <article class="post" style="left:612px">
    <div class="post-photo" role="img" aria-label="Photo of a festival-goer in a colourful hat at an outdoor concert" style="background:linear-gradient(180deg,#6c8aa8,#9a5a7a 45%,#3a2e2a)"></div>
    <div class="post-date">May<b>16</b></div>
    <h3 class="post-title deco">Foxtrot Lane sponsoring Riverside Rhythm Fest 2016</h3>
  </article>
  <div class="btn-small" style="left:510px;top:634px;width:180px;height:34px;line-height:34px;font-weight:600">Make an appointment</div>
</section>

<footer class="site-footer">
  <div class="foot-brand"><span class="brand-mark"></span><span class="brand-name">Foxtrot Lane</span></div>
  <div class="foot-tag">Classiest cleaners in Portland</div>
  <div class="foot-copy">Copyright 2018 Foxtrot Lane</div>
  <div class="foot-col" style="top:76px"><h6>Hours</h6>Monday – Saturday<br>Phone: 8:00 am – 6:00 pm</div>
  <div class="foot-col" style="top:136px"><h6>Location</h6>742 SE Larkspur Ave, Portland, OR 97214</div>
  <div class="foot-col" style="top:196px"><h6>Contact</h6>503-555-0148<br>hello@foxtrotlane.com</div>
  <div class="foot-about"><h6>About us</h6>Foxtrot Lane is a locally owned family business dedicated to providing you with quality cleaning services for a reasonable price. We clean homes and commercial buildings, inside and out, across the greater Portland area. Our crew takes pride in honest work, fair prices and a sparkling finish every time.</div>
  <div class="social"><span></span><span></span><span></span><span></span><span></span></div>
</footer>

</body>
</html>
```